TriVex Business Card Design - double sided -plumbing local plumbing company

We have a Plumbing company where the design was create through Sketch Hive. We would now like a business card designed as well. We want it to be in the colour version of the logo.

Details below for the card.

Phone Number: 0438 615 247
Email: info@trivexplumbing.example.au
Website: https://trivexplumbing.example.au
We really want a sophisticated design that stand out from the other- informative and timeless.

Target Market(s)

local Canberra market

Industry/Entity Type

Plumbing, gas fitting, hot water

Contact Information for Business Card

Phone number, email, logo and "Supplying all your heating, cooling and hot water needs"

Requirements
Must have
• bust be colourful, must also be though about it being printed on a magnet. must Vex with the logo - I dont want the logo and information chucked onto a white canvas I would prefer it to be smooth and look purposeful

```html
<!DOCTYPE html>
<html lang="en">
<head>
<meta charset="utf-8">
<title>TriVex Plumbing – Business Card</title>
<link rel="stylesheet" href="https://fonts.googleapis.com/css2?family=Exo+2:wght@700&family=Roboto:wght@400&display=swap">
<style>
  :root {
    --sky: #02aced;
    --amber: #fbb040;
    --paper: #ffffff;
    --backdrop: #e9e9e9;
  }
  * { box-sizing: border-box; margin: 0; padding: 0; }
  html, body {
    width: 1200px;
    height: 1200px;
    overflow: hidden;
    background: var(--backdrop);
  }
  .card {
    position: absolute;
    left: 149px;
    width: 901px;
    height: 527px;
    background: var(--paper);
    overflow: hidden;
  }
  .card--front { top: 54px; }
  .card--back { top: 625px; }

  .card__waves {
    position: absolute;
    inset: 0;
    width: 100%;
    height: 100%;
  }

  .brand {
    position: absolute;
    font-family: "Exo 2", sans-serif;
    font-weight: 700;
    color: var(--sky);
    text-align: center;
    line-height: 1;
  }
  .brand__name {
    display: block;
    font-size: 128px;
    letter-spacing: 0.02em;
  }
  .brand__trade {
    display: block;
    font-size: 34px;
    letter-spacing: 0.32em;
    margin-top: 10px;
    padding-left: 0.32em;
  }
  .card--front .brand { left: 60px; width: 620px; top: 52px; }
  .card--back .brand { left: 0; width: 100%; top: 172px; }

  .contact {
    position: absolute;
    right: 80px;
    top: 350px;
    list-style: none;
    font-family: "Roboto", sans-serif;
    font-size: 23px;
    color: var(--paper);
  }
  .contact__item {
    display: flex;
    justify-content: flex-end;
    align-items: center;
    gap: 16px;
    height: 41px;
  }
  .contact__icon {
    width: 18px;
    height: 18px;
    fill: var(--paper);
    flex: none;
  }
</style>
</head>
<body>

  <section class="card card--front" aria-label="Business card front">
    <svg class="card__waves" viewBox="0 0 721 422" preserveAspectRatio="none" aria-hidden="true">
      <path fill="var(--amber)" d="M0,175 C80,225 180,285 320,305 L320,422 L0,422 Z"/>
      <path fill="var(--sky)" d="M0,380 C130,392 225,330 300,255 C370,188 470,168 560,193 C632,214 690,258 721,302 L721,422 L0,422 Z"/>
    </svg>

    <div class="brand">
      <span class="brand__name">TriVex</span>
      <span class="brand__trade">PLUMBING</span>
    </div>

    <ul class="contact">
      <li class="contact__item">
        <span>0438 615 247</span>
        <svg class="contact__icon" viewBox="0 0 24 24" aria-hidden="true"><path d="M6.6 10.8a15.1 15.1 0 0 0 6.6 6.6l2.2-2.2a1 1 0 0 1 1-.25 11.4 11.4 0 0 0 3.6.57 1 1 0 0 1 1 1V20a1 1 0 0 1-1 1A17 17 0 0 1 3 4a1 1 0 0 1 1-1h3.5a1 1 0 0 1 1 1c0 1.25.2 2.45.57 3.57a1 1 0 0 1-.25 1z"/></svg>
      </li>
      <li class="contact__item">
        <span>info@trivexplumbing.example.au</span>
        <svg class="contact__icon" viewBox="0 0 24 24" aria-hidden="true"><path d="M3 5h18a1 1 0 0 1 1 1v12a1 1 0 0 1-1 1H3a1 1 0 0 1-1-1V6a1 1 0 0 1 1-1zm1 2.2V8l8 5 8-5v-.8l-8 5z"/></svg>
      </li>
      <li class="contact__item">
        <span>trivexplumbing.example.au</span>
        <svg class="contact__icon" viewBox="0 0 24 24" aria-hidden="true"><path d="M12 2a10 10 0 1 0 0 20 10 10 0 0 0 0-20zm6.9 6h-3a15.7 15.7 0 0 0-1.3-3.6A8 8 0 0 1 18.9 8zM12 4c.8 1.1 1.5 2.5 1.9 4h-3.8c.4-1.5 1.1-2.9 1.9-4zM4.3 14a8 8 0 0 1 0-4h3.4a16.5 16.5 0 0 0 0 4zm.8 2h3a15.7 15.7 0 0 0 1.3 3.6A8 8 0 0 1 5.1 16zm3-8h-3a8 8 0 0 1 4.3-3.6A15.7 15.7 0 0 0 8.1 8zM12 20c-.8-1.1-1.5-2.5-1.9-4h3.8c-.4 1.5-1.1 2.9-1.9 4zm2.3-6H9.7a14.7 14.7 0 0 1 0-4h4.6a14.7 14.7 0 0 1 0 4zm.3 5.6a15.7 15.7 0 0 0 1.3-3.6h3a8 8 0 0 1-4.3 3.6zm1.7-5.6a16.5 16.5 0 0 0 0-4h3.4a8 8 0 0 1 0 4z"/></svg>
      </li>
    </ul>
  </section>

  <section class="card card--back" aria-label="Business card back">
    <div class="brand">
      <span class="brand__name">TriVex</span>
      <span class="brand__trade">PLUMBING</span>
    </div>
  </section>

</body>
</html>
```